" O Carro Chefe são Pratos Congelados Sem Glúten, Sem Leite, Sem Soja e Sem Ovo com 70% de Produtos Orgânicos e além disso possuímos linhas com Baixa Carga Glicêmica e Baixo Colesterol "

```html
<!DOCTYPE html>
<html lang="pt-BR">
<head>
<meta charset="UTF-8">
<title>Verdalis – Pasta</title>
<link href="https://fonts.googleapis.com/css2?family=Oswald:wght@500;700&display=swap" rel="stylesheet">
<style>
  :root {
    --stage: #e4e4e4;
    --leaf: #5a8a2a;
    --leaf-dark: #4c7a22;
    --leaf-faint: #6e9a3c;
    --tomato: #e2452b;
    --paper: #f7f7f5;
    --white: #ffffff;
  }
  * { margin: 0; padding: 0; box-sizing: border-box; }
  html, body {
    width: 1200px; height: 1200px; overflow: hidden;
    background: var(--stage);
    font-family: "Oswald", sans-serif;
  }
  .folder {
    position: absolute; left: 130px; top: 230px;
    width: 940px; height: 740px;
    display: flex;
    box-shadow: 0 20px 50px rgba(0,0,0,0.18);
  }
  .cover { position: relative; width: 470px; height: 740px; overflow: hidden; }
  .cover--back { background: var(--leaf); }
  .cover--front { background: var(--paper); }

  .brand { text-align: center; line-height: 1; }
  .brand__name { font-weight: 700; letter-spacing: 1px; }
  .brand__tag { font-weight: 700; letter-spacing: 1.5px; }

  .brand--faint { position: absolute; top: 70px; left: 0; right: 0; color: var(--leaf-faint); }
  .brand--faint .brand__name { font-size: 96px; }
  .brand--faint .brand__tag { font-size: 30px; margin-top: 6px; }

  .back-signature { position: absolute; left: 60px; bottom: 210px; color: var(--white); }
  .back-signature .brand { text-align: left; }
  .back-signature .brand__name { font-size: 52px; }
  .back-signature .brand__tag { font-size: 15px; margin-top: 4px; }
  .contact { margin-top: 14px; font-weight: 500; font-size: 11px; line-height: 1.6; color: rgba(255,255,255,0.85); letter-spacing: 0.3px; }

  .brand--front { position: absolute; top: 250px; left: 0; right: 0; }
  .brand--front .brand__name { font-size: 92px; color: var(--tomato); }
  .brand--front .brand__tag { font-size: 26px; color: var(--leaf); margin-top: 6px; }

  .front-swoosh { position: absolute; left: 0; bottom: 0; width: 470px; height: 260px; }
</style>
</head>
<body>
  <main class="folder">
    <section class="cover cover--back">
      <div class="brand brand--faint">
        <div class="brand__name">Verdalis</div>
        <div class="brand__tag">GASTRONOMIA SAUDÁVEL</div>
      </div>
      <div class="back-signature">
        <div class="brand">
          <div class="brand__name">Verdalis</div>
          <div class="brand__tag">GASTRONOMIA SAUDÁVEL</div>
        </div>
        <div class="contact">
          <p>Rua das Flores, 120 – Centro</p>
          <p>Tel: (11) 4000-1234</p>
          <p>contato@verdalis.com.br</p>
        </div>
      </div>
    </section>
    <section class="cover cover--front">
      <div class="brand brand--front">
        <div class="brand__name">Verdalis</div>
        <div class="brand__tag">GASTRONOMIA SAUDÁVEL</div>
      </div>
      <svg class="front-swoosh" viewBox="0 0 470 260" preserveAspectRatio="none">
        <path d="M0 260 C160 230 340 170 470 40 L470 260 Z" fill="var(--tomato)"/>
        <path d="M0 260 C170 245 350 195 470 80 L470 260 Z" fill="var(--paper)"/>
        <path d="M40 260 C200 250 370 215 470 140 L470 260 Z" fill="var(--leaf)"/>
      </svg>
    </section>
  </main>
</body>
</html>
```